brochure for high-end senior living company

We need a new brochure that we can pass out to doctors and social workers so they would choose us over the competition.
brightmeadowhaven.example is our website that shows our colors and themes

we stand out over our competition due to our high quality of staff and our staff to resident ratio.
We are not afraid of difficult and complex care situations. Instead, we thrive on coordinating complexity.

We do all of this in a lovely setting that is luxurious and feels like home.

Target Market(s)

The families who make the decision are 60-70 years old. They are not not "rich" but they have saved well and usually have more than 1 million in assets.

Industry/Entity Type

Senior Living, Memory Care

Font styles to use
Serif

Colors
00AB8E
00BBA5
67D7C9
C6EFE9
E9F9F6
FFC000
F8CF3A
FAE287
FDF2CF
FEFAEE

Requirements
Must have
• When compromise is not an option...
Nice to have
• A difficult balance of beautiful and activities (happy people), but also communicating that we handle difficult and complex care.

```html
<!DOCTYPE html>
<html lang="en">
<head>
<meta charset="utf-8">
<title>Bright Meadow Haven – Tri-fold Brochure</title>
<link href="https://fonts.googleapis.com/css2?family=Playfair+Display:ital,wght@0,400;0,700;0,900;1,400&family=Source+Sans+3:wght@400;600;800&display=swap" rel="stylesheet">
<style>
:root{
  --backdrop:#c9c9c9;
  --teal:#00a088;
  --teal-deep:#008a75;
  --teal-bright:#00BBA5;
  --teal-mist:#E9F9F6;
  --gold:#e0b62c;
  --gold-soft:#F8CF3A;
  --ink:#0b6a5a;
  --white:#ffffff;
  --serif:"Playfair Display",Georgia,serif;
  --sans:"Source Sans 3","Helvetica Neue",Arial,sans-serif;
}
*{box-sizing:border-box;margin:0;padding:0}
html,body{width:854px;height:1200px;overflow:hidden;background:var(--backdrop)}
.canvas{position:relative;width:854px;height:1200px}
.sheet{position:absolute;left:40px;width:774px;height:547px;display:flex;box-shadow:0 6px 12px rgba(0,0,0,.35)}
.sheet--outside{top:33px}
.sheet--inside{top:626px}
.panel{position:relative;width:258px;height:100%;overflow:hidden}
.panel--teal{background:linear-gradient(90deg,var(--teal) 0%,var(--teal-deep) 100%)}

/* services */
.services{height:400px;padding:30px 26px 0 27px}
.title-gold{font-family:var(--serif);color:var(--gold-soft);font-weight:400;line-height:1.05}
.services h2{font-size:28px;margin-bottom:24px}
.services ul{list-style:none}
.services li{font-family:var(--sans);color:var(--white);font-size:14px;padding:0 0 3px 1px;margin-bottom:22px;position:relative}
.services li::after{content:"";position:absolute;left:-2px;bottom:-3px;width:190px;height:2px;background:linear-gradient(90deg,var(--gold-soft),rgba(248,207,58,0))}
.consult{position:absolute;left:0;top:399px;width:258px;height:148px;background:linear-gradient(90deg,#fff 40%,var(--teal-mist));padding:24px 16px 0 25px;font-family:var(--sans);font-weight:800;font-size:12.2px;line-height:1.43;color:var(--ink)}
.consult .phone{color:var(--gold)}

/* locations */
.locations{text-align:center;padding-top:35px}
.locations h2{font-family:var(--sans);font-weight:800;color:var(--white);font-size:13px;line-height:1.1;margin-bottom:6px}
.location{margin:0 auto 8px}
.photo-frame{width:118px;height:118px;margin:0 auto;border:2px solid var(--gold-soft);padding:3px}
.photo{width:100%;height:100%}
.photo--home{background:linear-gradient(180deg,#eef1f3 0%,#c9a99a 45%,#6b8c4a 80%,#4f7a34 100%)}
.photo--patio{background:linear-gradient(180deg,#93a57c 0%,#d7d1c0 45%,#8b8a6c 100%)}
.photo--court{background:linear-gradient(180deg,#f2f4f5 0%,#b5a28a 40%,#d9d6ce 70%,#e9e7e2 100%)}
.location address{font-style:normal;font-family:var(--sans);color:var(--white);font-size:10.5px;line-height:1.2;margin-top:3px}

/* cover */
.cover{background:linear-gradient(180deg,#fafbfd 0%,#e6eef8 20%,#a9c2e3 40%,#8eb0dc 55%,#e6e7ea 75%,#f2f2f4 100%)}
.cover-photo{position:absolute;left:0;top:255px;width:258px;height:150px;background:linear-gradient(180deg,rgba(0,0,0,0) 0%,#8c7b6b 22%,#d7c9a8 45%,#e9e2cf 70%,rgba(236,236,238,.9) 100%)}
.brand{position:absolute;top:40px;left:0;width:100%;text-align:center}
.brand-name{font-family:var(--serif);font-weight:400;color:var(--ink);font-size:22px;line-height:1;white-space:nowrap}
.brand-rule{width:206px;height:2px;background:var(--gold);margin:6px auto 5px}
.brand-sub{font-family:var(--serif);color:#2a3a35;font-size:14.5px}
.headline{position:absolute;top:383px;left:0;width:100%;text-align:center;color:var(--ink)}
.headline .lead{font-family:var(--serif);font-weight:400;font-size:24px;line-height:.92}
.headline .strong{font-family:var(--serif);font-weight:900;font-size:32px;line-height:.95}
.headline .tag{font-family:var(--sans);font-weight:600;color:#556;font-size:10.5px;margin-top:3px}

/* inside */
.story{padding:30px 25px 0 25px;text-align:center}
.story h2{font-size:23px;line-height:1.0;margin-bottom:8px}
.story p{font-family:var(--sans);color:var(--white);font-size:10.4px;line-height:1.27;text-align:justify;margin-bottom:3px}
.wide{position:relative;width:516px;height:100%;background:linear-gradient(90deg,#fff 0%,var(--teal-mist) 50%,#fff 50.2%,#eef8f6 100%)}
.promise{position:absolute;left:18px;top:150px;width:222px;text-align:center;font-family:var(--serif);font-style:italic;color:var(--ink);font-size:21px;line-height:1.2}
.promise::after{content:"";display:block;width:60px;height:2px;background:var(--gold);margin:14px auto 0}
.activity-photo{position:absolute;left:0;top:374px;width:516px;height:173px;background:linear-gradient(180deg,rgba(255,255,255,0) 0%,#7d9669 15%,#5d8d3f 55%,#8a8577 75%,#b0aaa2 100%)}
.reasons{position:absolute;left:278px;top:36px;width:238px}
.reasons h2{font-size:27px;line-height:.9;color:var(--gold);margin-bottom:36px}
.reason{display:flex;align-items:center;margin-bottom:36px}
.reason svg{width:34px;height:34px;flex:none;margin-right:12px}
.reason p{font-family:var(--sans);color:var(--ink);font-size:12.5px;line-height:1.15;flex:1;padding-bottom:3px;position:relative}
.reason p::after{content:"";position:absolute;left:0;bottom:-4px;width:100%;height:2px;background:linear-gradient(90deg,var(--gold),rgba(224,182,44,.1))}
</style>
</head>
<body>
<div class="canvas">

  <section class="sheet sheet--outside">
    <div class="panel panel--teal">
      <div class="services">
        <h2 class="title-gold">Our Services</h2>
        <ul>
          <li>Alzheimer’s &amp; Dementia Care</li>
          <li>Stroke Care</li>
          <li>Parkinson’s Care</li>
          <li>Limited Mobility</li>
          <li>Hospice Care</li>
          <li>Skin &amp; Incontinence Care</li>
          <li>Short Term Stays</li>
        </ul>
      </div>
      <div class="consult">Interested In Our Care &amp; Services?<br>Call <span class="phone">(555) 014-2290</span> Today To<br>Request A Free Consultation &amp;<br>Community Tour!</div>
    </div>

    <div class="panel panel--teal locations">
      <h2>Bright Meadow Haven Residential<br>Assisted Locations</h2>
      <div class="location">
        <div class="photo-frame"><div class="photo photo--home" role="img" aria-label="Photo of a single-story residential care home with lawn"></div></div>
        <address>412 Linden Crest Rd<br>Maple Hollow, CA 90001</address>
      </div>
      <div class="location">
        <div class="photo-frame"><div class="photo photo--patio" role="img" aria-label="Photo of a shaded patio with table and chairs"></div></div>
        <address>77 Sparrow Bend Ct,<br>Willow Ridge, CA 90002</address>
      </div>
      <div class="location">
        <div class="photo-frame"><div class="photo photo--court" role="img" aria-label="Photo of a home entrance with walkway"></div></div>
        <address>239 Quail Run Ln<br>Maple Hollow, CA 90001</address>
      </div>
    </div>

    <div class="panel cover">
      <div class="cover-photo" role="img" aria-label="Photo of a large stone-accented residential home under a blue sky"></div>
      <div class="brand">
        <div class="brand-name">Bright Meadow Haven</div>
        <div class="brand-rule"></div>
        <div class="brand-sub">Residential Assisted Living</div>
      </div>
      <div class="headline">
        <div class="lead">The Perfect<br>Balance of</div>
        <div class="strong">Safety &amp;<br>Warmth</div>
        <div class="tag">Trained Professionals who Provide Advanced Care</div>
      </div>
    </div>
  </section>

  <section class="sheet sheet--inside">
    <div class="panel panel--teal story">
      <h2 class="title-gold">Our Maple Hollow &amp; Cedar Bend Senior Caregivers are Compassionate and Attentive</h2>
      <p>Though it may be obvious that Bright Meadow Haven takes care of older folks, what’s not as evident is how we do it. We have had many people drive up and down our street and call us saying “I can’t find your building, there’s just a bunch of houses here.” It’s so common in our society that the elderly are mainly served in institutional, commercial, apartment-like buildings. We are used to it and chuckle as we explain that indeed, they are on the right street.</p>
      <h2 class="title-gold">Exceptional Care, Safety, and Customer Service</h2>
      <p>Bright Meadow Haven was started by and is operated by me (Aren) and I couldn’t do it without the help of my wife, Lena. We live locally in Maple Hollow with our three little children: Clara, Owen, and Ivy. We believe that every person, young and old, is created equal and deserves dignity. We believe that and set out to build a business that reflects that. The care, comfort, and happiness of our residents and their families is our daily pursuit.</p>
    </div>

    <div class="wide">
      <p class="promise">When compromise is not an option...</p>
      <div class="activity-photo" role="img" aria-label="Photo of residents, families and caregivers enjoying an outdoor gathering on a porch and lawn"></div>
      <div class="reasons">
        <h2 class="title-gold">Reasons to<br>Choose Us</h2>
        <div class="reason">
          <svg viewBox="0 0 34 34" aria-hidden="true"><g fill="#e0b62c"><rect x="2" y="8" width="3" height="20"/><rect x="2" y="21" width="30" height="4"/><rect x="29" y="21" width="3" height="7"/><circle cx="10" cy="16" r="3.5"/><path d="M15 13h13a4 4 0 0 1 4 4v3H15z"/></g></svg>
          <p>Private Rooms and Bathrooms</p>
        </div>
        <div class="reason">
          <svg viewBox="0 0 34 34" aria-hidden="true"><g fill="#e0b62c"><circle cx="17" cy="17" r="9"/><circle cx="17" cy="17" r="6" fill="#fff"/><circle cx="17" cy="17" r="4.5"/><rect x="3" y="6" width="2" height="22"/><rect x="29" y="6" width="3" height="22" rx="1.5"/></g></svg>
          <p>Delicious and Healthy<br>Home Cooked Meals</p>
        </div>
        <div class="reason">
          <svg viewBox="0 0 34 34" aria-hidden="true"><g fill="#e0b62c"><path d="M20 14c-4-3-7-5.5-7-8.5a3.5 3.5 0 0 1 7-1 3.5 3.5 0 0 1 7 1c0 3-3 5.5-7 8.5z"/><path d="M2 26l6-6c2-2 4-2 6-1l5 2h4a2 2 0 0 1 0 4h-6v1h7l6-5a2 2 0 0 1 2.5 3L25 30H11l-4 3z"/></g></svg>
          <p>Highest Caregiver to Resident<br>Ratio in the Industry</p>
        </div>
        <div class="reason">
          <svg viewBox="0 0 34 34" aria-hidden="true"><g fill="none" stroke="#e0b62c" stroke-width="2.5"><path d="M4 24a13 13 0 1 1 26 0"/><path d="M17 10v8h5"/></g><rect x="5" y="23" width="24" height="9" rx="1" fill="#e0b62c"/><text x="17" y="30.5" text-anchor="middle" font-family="Source Sans 3,sans-serif" font-size="7" font-weight="800" fill="#fff">24/7</text></svg>
          <p>24/7 Well-Trained Caregivers<br>in Site</p>
        </div>
      </div>
    </div>
  </section>

</div>
</body>
</html>
```